north lark upkeep services

Target Market(s)

General letter head for emails and letter quotes ect

Colors
0054AA
0677BA
7BADD7
CADEEF
E8F1F8
0094D4
00A9DD
6FCCEA
C7EBF8
E9F6FB

Requirements
Must have
• logo phone email website names
Nice to have
• what we do (from the website)

```html
<!DOCTYPE html>
<html lang="en">
<head>
<meta charset="utf-8">
<title>North Lark Upkeep Services – Letterhead</title>
<link href="https://fonts.googleapis.com/css2?family=Montserrat:wght@500;600;700;800&family=Open+Sans:wght@400;600&display=swap" rel="stylesheet">
<style>
  :root{
    --navy:#0054AA;
    --blue:#0677BA;
    --sky:#0094D4;
    --cyan:#00A9DD;
    --pale:#E8F1F8;
    --mist:#CADEEF;
    --ink:#1d1d22;
    --stage:#d9dadc;
    --paper:#ffffff;
  }
  *{box-sizing:border-box;margin:0;padding:0}
  html,body{width:1200px;height:1159px;overflow:hidden;background:var(--stage)}
  .letterhead{
    position:absolute;left:210px;top:28px;width:780px;height:1103px;
    background:var(--paper);overflow:hidden;
    font-family:"Open Sans",Arial,sans-serif;color:var(--ink);
    box-shadow:0 6px 24px rgba(0,0,0,.18);
  }
  .backdrop-mark{
    position:absolute;left:215px;top:300px;width:420px;height:420px;border-radius:50%;
    background:var(--pale);opacity:.55;
  }
  .brand{
    position:absolute;left:60px;top:150px;display:flex;align-items:center;gap:12px;
  }
  .brand-dot{width:34px;height:34px;border-radius:50%;background:var(--navy)}
  .brand-name{
    font-family:"Montserrat",Arial,sans-serif;font-weight:800;font-size:19px;
    line-height:1.1;color:var(--navy);text-transform:uppercase;width:170px;
  }
  .contact{
    position:absolute;left:470px;top:60px;padding-left:14px;
    border-left:2px solid var(--blue);font-size:12.5px;line-height:1.45;
  }
  .contact-title{
    font-family:"Montserrat",Arial,sans-serif;font-weight:700;font-size:13px;
    color:var(--blue);text-transform:uppercase;margin-bottom:1px;
  }
  .contact-row{display:flex;align-items:center;gap:7px}
  .contact-row svg{width:11px;height:11px;fill:var(--blue);flex:none}
  .letter{position:absolute;left:118px;top:330px;width:560px;font-size:13.2px;line-height:1.42;position:absolute}
  .date{margin-bottom:18px}
  .recipient{margin-left:12px;margin-bottom:20px}
  .salutation{font-size:16px;font-weight:600;margin-left:20px;margin-bottom:16px}
  .body p{margin-left:26px;margin-bottom:22px}
  .closing{margin-left:26px;margin-top:20px}
  .signature{
    margin-left:26px;margin-top:14px;width:190px;height:62px;
    background:linear-gradient(90deg,#efefef,#f7f7f7);border-radius:4px;
  }
  .services-band{
    position:absolute;left:0;bottom:70px;width:100%;height:150px;
    background:linear-gradient(90deg,var(--navy) 0%,var(--blue) 55%,var(--sky) 100%);
    clip-path:polygon(0 45%,100% 0,100% 100%,0 100%);
  }
  .services{
    position:absolute;left:40px;bottom:84px;width:590px;
    font-family:"Montserrat",Arial,sans-serif;font-weight:500;font-size:11px;line-height:1.6;color:#fff;
  }
  .band-mark{
    position:absolute;right:34px;bottom:175px;width:78px;height:78px;border-radius:50%;
    background:var(--navy);border:5px solid var(--paper);
  }
</style>
</head>
<body>
<main class="letterhead">
  <div class="backdrop-mark" aria-hidden="true"></div>

  <header>
    <div class="brand">
      <span class="brand-dot" aria-hidden="true"></span>
      <span class="brand-name">North Lark Upkeep Services</span>
    </div>
    <address class="contact" style="font-style:normal">
      <div class="contact-title">North Lark Upkeep Services</div>
      <div>48 Harbor Row, Suite 5</div>
      <div>Alder Falls, Oregon 97012</div>
      <div class="contact-row"><svg viewBox="0 0 24 24"><path d="M6.6 10.8a15 15 0 0 0 6.6 6.6l2.2-2.2c.3-.3.7-.4 1-.2 1.1.4 2.3.6 3.6.6.6 0 1 .4 1 1V20c0 .6-.4 1-1 1A17 17 0 0 1 3 4c0-.6.4-1 1-1h3.5c.6 0 1 .4 1 1 0 1.3.2 2.5.6 3.6.1.3 0 .7-.2 1z"/></svg>+1 555 0142 700</div>
      <div class="contact-row"><svg viewBox="0 0 24 24"><path d="M2 5h20v14H2zm2 2v.5l8 5 8-5V7l-8 5z"/></svg>info@northlarkupkeep.com</div>
      <div class="contact-row"><svg viewBox="0 0 24 24"><circle cx="12" cy="12" r="10"/></svg>www.northlarkupkeep.com</div>
    </address>
  </header>

  <section class="letter">
    <div class="date">August-29-2024</div>
    <div class="recipient">Fern Hollow Co.<br>123 Street Name, Suite# 10<br>City, State, 120023</div>
    <div class="salutation">Dear Mr. Ellis</div>
    <div class="body">
      <p>Lorem ipsum dolor sit amet, consectetur adipisicing elit, sed do eiusmod tempor incididunt ut labore et dolore magna aliqua. Ut enim ad minim veniam, quis nostrud exercitation ullamco laboris nisi ut aliquip ex ea commodo consequat. Duis aute irure dolor in reprehenderit in voluptate velit esse cillum dolore eu fugiat nulla pariatur.</p>
      <p>Lorem ipsum dolor sit amet, consectetur adipisicing elit, sed do eiusmod tempor incididunt ut labore et dolore magna aliqua. Ut enim ad minim veniam, quis nostrud exercitation ullamco laboris nisi ut aliquip ex ea commodo consequat. Duis aute irure dolor in reprehenderit in voluptate velit esse cillum dolore eu fugiat nulla pariatur.</p>
      <p>Lorem ipsum dolor sit amet, consectetur adipisicing elit, sed do eiusmod tempor incididunt ut labore et dolore magna aliqua. Ut enim ad minim veniam, quis nostrud exercitation ullamco laboris nisi ut aliquip ex ea commodo consequat.</p>
      <p>Excepteur sint occaecat cupidatat non proident, sunt in culpa qui officia deserunt mollit anim id est laborum. re et dolore magnam aliquam quaerat voluptatem.</p>
    </div>
    <div class="closing">Regards</div>
    <div class="signature" role="img" aria-label="Handwritten signature of the sender"></div>
  </section>

  <footer>
    <div class="services-band" aria-hidden="true"></div>
    <span class="band-mark" aria-hidden="true"></span>
    <p class="services">• Roof Cleaning • Internal/External window cleaning • General cleaning • High clean (High Dusting) • Gutter Cleaning • Pressure/Rotary Cleaning • Soft Wash Building Cleaning • Netball/Basketball Court both Grass and Artificial • Graffiti removal • External Window Cleaning • Solar Pannel Cleaning • Car Park Cleaning • Sweep and Scrubber Machinery</p>
  </footer>
</main>
</body>
</html>
```